Vor Business Card

we need a business card for flooring business called Vor Flooring, the design should be black and white. we have 2 locations

Linwood Showroom
274 Kellaway Road,
Linwood VIC 3149

Ashcombe Showroom
592 Tarrant Hwy,
Ashcombe VIC 3187

email : sales@vorflooring.com.au
(03) 9517 2643

Please inform we sell , Laminate, Hybrid, Timber, carpet and commercial flooring

```html
<!DOCTYPE html>
<html lang="en">
<head>
<meta charset="utf-8">
<title>Vor Flooring Business Card</title>
<link rel="stylesheet" href="https://fonts.googleapis.com/css2?family=Poppins:wght@400;700&display=swap">
<style>
  :root {
    --stage: #2b2b2d;
    --ink: #141414;
    --paper: #ffffff;
    --card-black: #1c1a1b;
    --emboss: #3e3c3d;
    --muted: #222222;
  }
  * { box-sizing: border-box; margin: 0; padding: 0; }
  html, body { width: 1200px; height: 801px; overflow: hidden; }
  body {
    background: var(--stage);
    font-family: "Poppins", sans-serif;
    position: relative;
  }
  .card {
    position: absolute;
    top: 241px;
    width: 520px;
    height: 318px;
    overflow: hidden;
  }
  .card--back { left: 60px; background: var(--card-black); }
  .card--front { left: 620px; background: var(--paper); color: var(--ink); }

  .brand {
    font-weight: 400;
    letter-spacing: 3px;
    text-transform: uppercase;
    line-height: 1.15;
  }
  .card--back .brand {
    position: absolute;
    left: 0; right: 0; top: 120px;
    text-align: center;
    font-size: 40px;
    color: var(--emboss);
  }
  .card--front .brand {
    position: absolute;
    left: 34px; top: 100px;
    width: 220px;
    font-size: 36px;
    color: var(--ink);
  }

  .contact {
    position: absolute;
    left: 290px; top: 36px;
    width: 215px;
    font-size: 12px;
    line-height: 1.35;
    color: var(--muted);
  }
  .contact__item {
    display: flex;
    align-items: flex-start;
    margin-bottom: 14px;
  }
  .contact__icon {
    flex: none;
    width: 18px;
    padding-right: 6px;
    margin-right: 8px;
    border-right: 1px solid var(--muted);
    display: flex;
    flex-direction: column;
    gap: 4px;
    padding-top: 2px;
  }
  .contact__icon svg { width: 11px; height: 13px; display: block; }
  .contact__title { font-weight: 700; }

  .services {
    position: absolute;
    left: 0; right: 0; top: 244px;
    height: 40px;
    background: var(--ink);
    color: var(--paper);
    font-size: 13px;
    line-height: 40px;
    padding-left: 34px;
    white-space: nowrap;
  }
</style>
</head>
<body>
  <section class="card card--back" aria-label="Card back">
    <div class="brand">Vor Flooring</div>
  </section>

  <section class="card card--front" aria-label="Card front">
    <div class="brand">Vor<br>Flooring</div>

    <div class="contact">
      <div class="contact__item">
        <span class="contact__icon">
          <svg viewBox="0 0 12 14"><path d="M6 1a4 4 0 0 0-4 4c0 3 4 8 4 8s4-5 4-8a4 4 0 0 0-4-4z" fill="none" stroke="#222" stroke-width="1.4"/><circle cx="6" cy="5" r="1.4" fill="#222"/></svg>
        </span>
        <div>
          <div class="contact__title">Ashcombe Showroom</div>
          <div>592 Tarrant Hwy,</div>
          <div>Ashcombe VIC 3187</div>
        </div>
      </div>
      <div class="contact__item">
        <span class="contact__icon">
          <svg viewBox="0 0 12 14"><path d="M6 1a4 4 0 0 0-4 4c0 3 4 8 4 8s4-5 4-8a4 4 0 0 0-4-4z" fill="none" stroke="#222" stroke-width="1.4"/><circle cx="6" cy="5" r="1.4" fill="#222"/></svg>
        </span>
        <div>
          <div class="contact__title">Linwood Showroom</div>
          <div>274 Kellaway Road,</div>
          <div>Linwood VIC 3149</div>
        </div>
      </div>
      <div class="contact__item">
        <span class="contact__icon">
          <svg viewBox="0 0 12 10"><rect x="0.5" y="1" width="11" height="8" fill="#222"/><path d="M1 1.5l5 4 5-4" fill="none" stroke="#fff" stroke-width="1"/></svg>
          <svg viewBox="0 0 12 12"><path d="M3 1l2 2.5-1.2 1.3c.7 1.5 1.9 2.7 3.4 3.4L8.5 7 11 9l-1.3 2C5.5 11 1 6.5 1 2.3z" fill="#222"/></svg>
        </span>
        <div>
          <div>sales@vorflooring.com.au</div>
          <div>(03) 9517 2643</div>
        </div>
      </div>
    </div>

    <div class="services">we sell | Laminate | Hybrid | Timber | Carpet and Commercial Flooring</div>
  </section>
</body>
</html>
```